Cosmetics Brand Logo and Bottle Label Design

We are creating a new cosmetics brand called "Nolan Whitby" and would like you to create an amazing logo and bottle label for this brand's new 100% pure argan oil product.
For the logo, we really like the logo's of Marin Calloway and Vessa. The text should be Sans Serif (without feet).
For the actual bottle label, please find attached labels of one of our competitors design which really like. We really like the simplicity and elegance of the design. The only difference is that our product will be using light turqoise as the brand color. Please feel free to add your own creativity into it as well.
Industry/Entity Type
Cosmetics
Logo Text
Nolan Whitby
Font styles to use

```html
<!DOCTYPE html>
<html lang="en">
<head>
<meta charset="utf-8">
<title>Nolan Whitby – Logo and Argan Oil Label</title>
<link rel="stylesheet" href="https://fonts.googleapis.com/css2?family=Didact+Gothic&family=Great+Vibes&display=swap">
<style>
  :root {
    --paper: #ffffff;
    --ink: #1c1a1b;
    --label-teal: #86d1c6;
    --script-teal: #3dbfa9;
    --label-white: #ffffff;
  }
  * { margin: 0; padding: 0; box-sizing: border-box; }
  html, body {
    width: 1200px;
    height: 889px;
    overflow: hidden;
    background: var(--paper);
  }
  .canvas {
    position: relative;
    width: 1200px;
    height: 889px;
    font-family: "Didact Gothic", sans-serif;
  }

  /* Wordmark */
  .wordmark {
    position: absolute;
    left: 415px;
    top: 228px;
    width: 623px;
    height: 61px;
  }
  .wordmark-frame {
    position: absolute;
    left: 30px;
    top: 0;
    right: 0;
    bottom: 0;
    border: 2px solid var(--ink);
  }
  .wordmark-dot {
    position: absolute;
    left: 0;
    top: 0;
    width: 61px;
    height: 61px;
    border-radius: 50%;
    border: 3px solid var(--ink);
    background: var(--paper);
  }
  .wordmark-name {
    position: absolute;
    left: 66px;
    top: 2px;
    font-size: 60px;
    line-height: 58px;
    color: var(--ink);
    letter-spacing: 1px;
    white-space: nowrap;
  }

  /* Label */
  .label {
    position: absolute;
    left: 452px;
    top: 346px;
    width: 367px;
    height: 443px;
    background: var(--label-teal);
    color: var(--label-white);
  }
  .spine {
    position: absolute;
    transform-origin: top left;
    transform: rotate(-90deg);
    white-space: nowrap;
  }
  .label-brand {
    left: 78px;
    top: 395px;
    width: 331px;
    height: 45px;
    display: flex;
    align-items: center;
  }
  .label-brand-dot {
    width: 34px;
    height: 34px;
    border-radius: 50%;
    border: 2px solid var(--label-white);
    flex: none;
    margin-right: 4px;
  }
  .label-brand-name {
    border: 1.5px solid var(--label-white);
    padding: 0 4px;
    font-size: 34px;
    line-height: 40px;
  }
  .label-tagline {
    left: 125px;
    top: 314px;
    width: 250px;
    height: 30px;
    font-size: 25px;
    line-height: 30px;
  }
  .label-variant {
    left: 168px;
    top: 354px;
    width: 320px;
    height: 110px;
    font-family: "Great Vibes", cursive;
    font-size: 112px;
    line-height: 110px;
    color: var(--script-teal);
    text-align: center;
  }
  .label-descriptor {
    position: absolute;
    left: 174px;
    top: 364px;
    font-size: 16px;
    line-height: 19px;
  }
</style>
</head>
<body>
  <main class="canvas">
    <div class="wordmark">
      <div class="wordmark-frame"></div>
      <div class="wordmark-dot"></div>
      <div class="wordmark-name">NOLAN WHITBY</div>
    </div>

    <section class="label">
      <div class="spine label-brand">
        <span class="label-brand-dot"></span>
        <span class="label-brand-name">NOLAN WHITBY</span>
      </div>
      <div class="spine label-tagline">100% pure argan oil</div>
      <div class="spine label-variant">Light</div>
      <p class="label-descriptor">ultra lightweight<br>moisturizing oil</p>
    </section>
  </main>
</body>
</html>
```